Marrowfield Contracting Business Cards

Front of card:

Full Logo
Name
Address
Office Phone
Cell Phone
Email
Website

Back:
Logo Mark in background
List and markets and services performed

```html
<!DOCTYPE html>
<html lang="en">
<head>
<meta charset="utf-8">
<title>Marrowfield Contracting Business Cards</title>
<link rel="stylesheet" href="https://fonts.googleapis.com/css2?family=Montserrat:wght@600;700&family=Poppins:wght@400;500&family=Michroma&family=Saira:wght@400&display=swap">
<style>
  :root {
    --brand-red: #d71f27;
    --brand-gray: #6b6b6b;
    --text-gray: #555555;
    --card-white: #ffffff;
    --faint-red: #e0534f;
    --page-bg: #e9e6e1;
  }
  * { margin: 0; padding: 0; box-sizing: border-box; }
  html, body { width: 900px; height: 1200px; overflow: hidden; }
  body { background: var(--page-bg); position: relative; font-family: "Poppins", sans-serif; }

  .card {
    position: absolute; left: 81px; width: 736px; height: 427px;
    border-radius: 18px; overflow: hidden;
    box-shadow: 0 4px 12px rgba(0,0,0,0.25);
  }
  .card-front { top: 126px; background: var(--card-white); }
  .card-back { top: 637px; background: var(--brand-red); }

  /* Front */
  .logo-tab { position: absolute; left: 0; top: 44px; width: 44px; height: 92px; background: var(--brand-red); }
  .logo-dot {
    position: absolute; left: 48px; top: 44px; width: 92px; height: 92px;
    border-radius: 50%; background: var(--card-white); border: 9px solid var(--brand-red);
  }
  .company-name {
    position: absolute; left: 166px; top: 58px;
    font-family: "Montserrat", sans-serif; font-weight: 700; color: var(--brand-red);
    font-size: 25px; line-height: 26px; letter-spacing: 0.5px;
  }
  .company-name .suffix { display: block; font-size: 12px; line-height: 16px; text-align: right; letter-spacing: 2px; }
  .company-rule { position: absolute; left: 166px; top: 125px; width: 172px; height: 2px; background: var(--brand-gray); }

  .mark-ring {
    position: absolute; left: 450px; top: 5px; width: 320px; height: 320px;
    border-radius: 50%; border: 26px solid var(--brand-red);
  }

  .person-name {
    position: absolute; left: 46px; top: 196px;
    font-family: "Montserrat", sans-serif; font-weight: 600; font-size: 23px;
    color: var(--brand-gray); letter-spacing: 0.5px;
  }
  .person-title {
    position: absolute; left: 46px; top: 224px;
    font-family: "Montserrat", sans-serif; font-weight: 700; font-size: 16px;
    color: var(--brand-red); letter-spacing: 0.5px;
  }
  .contact-list { position: absolute; left: 46px; top: 259px; list-style: none; }
  .contact-list li {
    display: flex; align-items: center; height: 22.5px;
    font-size: 16px; color: var(--text-gray);
  }
  .contact-list svg { width: 14px; height: 14px; margin-right: 8px; fill: var(--brand-red); }

  .address-band {
    position: absolute; left: 0; bottom: 0; width: 100%; height: 53px;
    background: var(--brand-red); color: var(--card-white);
    display: flex; align-items: center; justify-content: center;
    font-size: 16px; font-weight: 500; padding-left: 20px;
  }

  /* Back */
  .mark-ghost {
    position: absolute; left: 372px; top: 50px; width: 360px; height: 360px;
    border-radius: 50%; border: 40px solid var(--faint-red);
  }
  .services-title {
    position: absolute; left: 43px; top: 44px;
    font-family: "Michroma", sans-serif; font-size: 20px; color: var(--card-white);
    letter-spacing: 0.5px;
  }
  .services-list { position: absolute; left: 43px; top: 78px; list-style: none; }
  .services-list li {
    position: relative; padding-left: 20px; height: 25.8px; line-height: 25.8px;
    font-family: "Saira", sans-serif; font-size: 15.5px; color: var(--card-white); letter-spacing: 0.3px;
  }
  .services-list li::before {
    content: ""; position: absolute; left: 0; top: 8.5px;
    width: 9px; height: 9px; border-radius: 50%; background: var(--card-white);
  }
</style>
</head>
<body>

<section class="card card-front">
  <div class="logo-tab"></div>
  <div class="logo-dot"></div>
  <div class="company-name">MARROWFIELD<br>CONTRACTING<span class="suffix">LLC</span></div>
  <div class="company-rule"></div>

  <div class="mark-ring"></div>

  <div class="person-name">DANIEL WHITCOMBE</div>
  <div class="person-title">CEO/FOUNDER</div>

  <ul class="contact-list">
    <li><svg viewBox="0 0 24 24"><path d="M6.6 10.8a15 15 0 0 0 6.6 6.6l2.2-2.2c.3-.3.7-.4 1-.2 1.1.4 2.3.6 3.6.6.6 0 1 .4 1 1V20c0 .6-.4 1-1 1A17 17 0 0 1 3 4c0-.6.4-1 1-1h3.5c.6 0 1 .4 1 1 0 1.3.2 2.5.6 3.6.1.3 0 .7-.2 1z"/></svg>555.014.2087</li>
    <li><svg viewBox="0 0 24 24"><path d="M7 1h10a2 2 0 0 1 2 2v18a2 2 0 0 1-2 2H7a2 2 0 0 1-2-2V3a2 2 0 0 1 2-2zm0 3v14h10V4zm5 15.5a1.2 1.2 0 1 0 0 2.4 1.2 1.2 0 0 0 0-2.4z"/></svg>555.014.2087</li>
    <li><svg viewBox="0 0 24 24"><path d="M2 5h20v2l-10 6L2 7zm0 4.3l10 6 10-6V19H2z"/></svg>daniel@marrowfieldco.com</li>
    <li><svg viewBox="0 0 24 24"><path d="M12 2a10 10 0 1 0 0 20 10 10 0 0 0 0-20zm6.9 6h-2.9a15 15 0 0 0-1.4-3.6A8 8 0 0 1 18.9 8zM12 4c.8 1.2 1.5 2.5 1.9 4h-3.8c.4-1.5 1.1-2.8 1.9-4zM4.3 14a8 8 0 0 1 0-4h3.4a16 16 0 0 0 0 4zm.8 2h2.9c.3 1.3.8 2.5 1.4 3.6A8 8 0 0 1 5.1 16zM8 8H5.1a8 8 0 0 1 4.3-3.6C8.8 5.5 8.3 6.7 8 8zm4 12c-.8-1.2-1.5-2.5-1.9-4h3.8c-.4 1.5-1.1 2.8-1.9 4zm2.3-6H9.7a14 14 0 0 1 0-4h4.6a14 14 0 0 1 0 4zm.3 5.6c.6-1.1 1.1-2.3 1.4-3.6h2.9a8 8 0 0 1-4.3 3.6zm1.7-5.6a16 16 0 0 0 0-4h3.4a8 8 0 0 1 0 4z"/></svg>www.marrowfieldco.com</li>
  </ul>

  <div class="address-band">418 Calder Street, Suite 210, Halbrook, MI 49620</div>
</section>

<section class="card card-back">
  <div class="mark-ghost"></div>
  <h2 class="services-title">OUR SERVICES</h2>
  <ul class="services-list">
    <li>Renewable Energy Projects</li>
    <li>Self Driving Car Engineer</li>
    <li>Digital Transformation with Nimbus Cloud</li>
    <li>Additive Manufacturing (3D Printing)</li>
    <li>Modern Building Design</li>
    <li>Industrial Internet of Things (IIoT)</li>
    <li>Digital Twins</li>
    <li>Renewable Energy Projects</li>
    <li>Self Driving Car Engineer</li>
    <li>Digital Transformation with Nimbus Cloud</li>
    <li>Additive Manufacturing (3D Printing)</li>
    <li>Modern Building Design</li>
  </ul>
</section>

</body>
</html>
```